Business Card

Need business cards and small flyers for a musical band

Target Market(s)

Promoters, clients seeking to hire a Latin band

Industry/Entity Type

Business

Requirements
Must have
• The name of the band is Orchestra Brisa so want to have the background with a fire design, with black card and the name of the band in RED, maybe a combination of Red with some yellow. See attached idea.
Nice to have
• See attached files for some ideas.

```html
<!DOCTYPE html>
<html lang="en">
<head>
<meta charset="utf-8">
<title>Orchestra Brisa — Business Card</title>
<link href="https://fonts.googleapis.com/css2?family=Oswald:wght@500;600&display=swap" rel="stylesheet">
<style>
  :root {
    --page-bg: #ecebe8;
    --card-black: #0b0c0d;
    --accent-red: #e3262b;
  }
  * { margin: 0; padding: 0; box-sizing: border-box; }
  html, body {
    width: 1200px;
    height: 1000px;
    overflow: hidden;
    background: var(--page-bg);
  }
  .business-card {
    position: absolute;
    left: 75px;
    top: 200px;
    width: 1050px;
    height: 600px;
    background: var(--card-black);
    font-family: "Oswald", "Arial Narrow", sans-serif;
    color: var(--accent-red);
    box-shadow: 0 6px 18px rgba(0,0,0,0.18);
  }
  .band-name {
    position: absolute;
    left: 0;
    right: 0;
    top: 95px;
    text-align: center;
    font-size: 112px;
    font-weight: 600;
    line-height: 1;
    letter-spacing: 1px;
  }
  .title-row {
    position: absolute;
    left: 190px;
    top: 290px;
    display: flex;
    align-items: center;
    gap: 16px;
  }
  .rule {
    display: block;
    height: 2px;
    background: var(--accent-red);
  }
  .rule-left { width: 110px; }
  .rule-right { width: 250px; }
  .role-title {
    font-size: 40px;
    font-weight: 600;
    letter-spacing: 0.5px;
    line-height: 1;
    white-space: nowrap;
  }
  .phone {
    position: absolute;
    left: 730px;
    top: 370px;
    font-size: 42px;
    font-weight: 500;
    letter-spacing: 2px;
    line-height: 1;
    white-space: nowrap;
  }
  .person-name {
    position: absolute;
    left: 100px;
    top: 470px;
    font-size: 46px;
    font-weight: 600;
    letter-spacing: 0.5px;
    line-height: 1;
    white-space: nowrap;
  }
</style>
</head>
<body>
  <section class="business-card">
    <h1 class="band-name">Orchestra Brisa</h1>
    <div class="title-row">
      <span class="rule rule-left"></span>
      <div class="role-title">MUSICAL DIRECTOR</div>
      <span class="rule rule-right"></span>
    </div>
    <div class="phone">(555)-210-3378</div>
    <div class="person-name">RAFAEL MONTOYA</div>
  </section>
</body>
</html>
```